Modernize and improve usability of our webpage www.lerntausch-brolani.ch (4 languages, mostly static content)

Need to modernize and freshen up the webpages of our association: www.lerntausch-brolani.ch We offer apprenticeship exchanges within Switzerland and abroad. Young people can inform and enroll online. We do the matchmaking with work locations and organize logistics, stay overs etc.
The webpage needs to be in 4 languages (German, French, Italian and English). The main pages will be:
- Landing page: what we do, targeted to our apprentices / young people who enroll for the stages.
- Sup-Page: Registration form for interested apprentices to sign up for the program
- Sub-Page "Company", the firms who would like to send their apprentices on a internship and info on how to join the program
- Sub-Page "Host Family", private people who would be interested in hosting the apprentices (for free) during the stages. Find out about the reqiurements for the host families
- Sub-Page "About Us", who we are, executive team, board of director, our sponsor "Harmil Circle Switzerland"
- Footer: contact (E-Mail, Telephone, WhatsApp), Bank details (IBAN Number), Partnerlogo of Harmil-Circle (see uploaded jpg), Social-Media Links (Facebook, LinkedIn)

Target Market(s)

Young people looking for a "apprenticeship" stage within Switzerland or going from Switzerland abroad

Industry/Entity Type

Apprenticeships: cooks, builders, craftsman, office support, etc.

Number of Pages Required

5+ page

Font styles to use
Other font styles liked:
• Lato (sans serif)

Requirements
Must have
• use colors shown on uploaded PDF-Slides: Make the BLUE the MAIN color, the ORANGE as a secondary color
Nice to have
• Forms using e.g. google forms or survey-monkey forms (external links, no code). Matching & appealing visuals showing young apprentices (can use stock photos)

```html
<!DOCTYPE html>
<html lang="en">
<head>
<meta charset="utf-8">
<title>brolani – Apprenticeship Exchange</title>
<link href="https://fonts.googleapis.com/css2?family=Lato:wght@400;700;900&family=Montserrat:wght@700;800;900&display=swap" rel="stylesheet">
<style>
:root{
  --blue:#1f56a3;
  --blue-dark:#173f7a;
  --navy:#13294d;
  --orange:#f36c21;
  --orange-soft:#f79a5c;
  --grey:#f1f2f4;
  --line:#d9dde3;
  --text:#2b3445;
  --muted:#6b7484;
  --white:#ffffff;
}
*{box-sizing:border-box;margin:0;padding:0}
html,body{width:776px;height:1200px;overflow:hidden;background:var(--white);font-family:"Lato",sans-serif;color:var(--text)}
.page{position:absolute;top:0;width:380px;height:1200px;overflow:hidden}
.page--home{left:0}
.page--companies{left:396px}
.band{position:absolute;left:0;width:380px;overflow:hidden}
.photo{position:absolute}
h1,h2,h3,.display{font-family:"Montserrat",sans-serif;font-weight:800;letter-spacing:.2px}

/* nav */
.nav{top:0;height:22px;background:var(--orange);display:flex;align-items:center;padding:0 12px;gap:8px}
.brand{font-family:"Lato",sans-serif;font-weight:900;color:var(--white);font-size:13px;display:flex;align-items:center;gap:4px}
.brand-dot{width:7px;height:7px;border-radius:50%;background:var(--white)}
.nav-links{margin-left:auto;display:flex;gap:7px;font-size:4.5px;color:var(--white);text-transform:uppercase;font-weight:700}
.nav-btn{background:var(--white);color:var(--orange);font-size:4.5px;font-weight:700;padding:2px 5px;border-radius:2px}

/* home hero */
.hero{top:22px;height:170px}
.hero .photo{inset:0;background:linear-gradient(100deg,#cfd6de 0%,#e8ebef 45%,#f6f7f8 100%)}
.hero-copy{position:absolute;right:14px;top:48px;width:150px;text-align:right}
.hero-copy h1{font-size:10px;line-height:1.25;color:var(--blue-dark);text-transform:uppercase}
.btn{display:inline-block;background:var(--orange);color:var(--white);font-size:5px;font-weight:700;padding:3px 9px;border-radius:2px;text-transform:uppercase;margin-top:7px}
.dots{position:absolute;left:50%;bottom:8px;display:flex;gap:3px;transform:translateX(-50%)}
.dots i{width:4px;height:4px;border-radius:50%;background:var(--white);opacity:.7}
.dots i:first-child{background:var(--orange);opacity:1}

/* features */
.features{top:192px;height:140px;background:var(--blue)}
.features h2,.companies h2{text-align:center;color:var(--white);font-size:11px;margin-top:30px}
.icons{display:flex;justify-content:space-around;padding:0 14px;margin-top:12px}
.icon-item{display:flex;flex-direction:column;align-items:center;width:60px;gap:4px}
.icon-item svg{width:26px;height:26px}
.icon-item span{font-size:4.5px;color:var(--white);text-align:center;line-height:1.3}
.wave{position:absolute;left:0;width:380px}

/* intro */
.intro{top:332px;height:178px}
.intro-text{position:absolute;left:16px;top:52px;width:150px;font-size:5px;line-height:1.55;color:var(--muted)}
.intro .photo{right:40px;top:20px;width:150px;height:150px;border-radius:50%;background:radial-gradient(circle at 50% 40%,#e4e8ee,#b9c3d1)}
.arc{position:absolute}

/* cards */
.cards{top:510px;height:122px;display:flex}
.card{flex:1;position:relative;padding:30px 18px 0;color:var(--white);text-align:center}
.card--blue{background:var(--blue)}
.card--orange{background:var(--orange)}
.card-badge{position:absolute;top:-2px;left:50%;transform:translateX(-50%);width:22px;height:22px;border-radius:50%;background:var(--white);display:flex;align-items:center;justify-content:center}
.card h3{font-size:7px;margin-bottom:5px;text-transform:uppercase}
.card p{font-size:4.5px;line-height:1.55;opacity:.9}

/* stories */
.stories{top:632px;height:140px}
.stories .photo{inset:0;background:linear-gradient(180deg,#3d4f6b,#24344f)}
.stories-names{position:absolute;inset:0;display:flex;align-items:center;justify-content:space-around}
.stories-names h2{color:var(--white);font-size:17px;line-height:1.05;text-transform:uppercase;text-align:center}

/* mobility */
.mobility{top:772px;height:205px}
.mobility .photo{left:26px;top:32px;width:130px;height:130px;border-radius:50%;background:radial-gradient(circle at 50% 40%,#dfe4ea,#a9b6c6)}
.mobility-copy{position:absolute;left:186px;top:46px;width:175px}
.mobility-copy h3{font-size:8px;color:var(--navy);line-height:1.3}
.ticks{list-style:none;margin-top:8px}
.ticks li{display:flex;align-items:center;gap:4px;font-size:4.8px;color:var(--muted);margin-bottom:4px}
.ticks li::before{content:"";width:5px;height:5px;border-radius:50%;background:var(--orange);flex:none}

/* apply */
.apply{background:var(--navy);display:flex;align-items:center;gap:18px}
.apply--home{top:977px;height:100px;padding-left:70px}
.apply--companies{top:752px;height:218px;padding-left:90px}
.apply h2{color:var(--white);font-size:14px}
.apply .btn{margin-top:6px}

/* footer */
.footer{background:var(--blue-dark);color:var(--white)}
.footer--home{top:1077px;height:123px}
.footer--companies{top:970px;height:168px}
.footer-cols{display:flex;gap:12px;padding:14px 14px 0}
.footer-col{flex:1;font-size:4.5px;line-height:1.6;opacity:.9}
.footer-col .brand{font-size:12px;margin-bottom:4px}
.footer-col h4{font-size:5px;font-weight:700;margin-bottom:3px;text-transform:uppercase}
.field{height:7px;background:var(--white);opacity:.9;border-radius:1px;margin-bottom:3px}
.partners{position:absolute;left:0;right:0;background:var(--white);display:flex;align-items:center;justify-content:flex-end;gap:10px;padding-right:14px}
.footer--home .partners{bottom:16px;height:24px}
.footer--companies .partners{bottom:26px;height:28px}
.partner{width:34px;height:10px;border-radius:2px;background:#c7ccd4}
.partner--round{width:12px;height:12px;border-radius:50%}
.copyright{position:absolute;left:0;right:0;bottom:5px;text-align:center;font-size:4px;opacity:.7}
.footer--companies .copyright{bottom:10px}

/* companies page */
.sub-hero{top:22px;height:108px}
.sub-hero .photo{inset:0;background:linear-gradient(180deg,#2a5fa8,#1b4585)}
.sub-hero h1{position:absolute;top:44px;width:100%;text-align:center;color:var(--white);font-size:12px}
.companies{top:130px;height:190px}
.companies .blueband{position:absolute;left:0;right:0;top:28px;height:140px;background:var(--blue)}
.companies h2{position:relative;margin-top:48px}
.companies .icons{position:relative}
.profile{top:320px;height:195px}
.profile h2{position:absolute;left:16px;top:40px;font-size:10px;color:var(--navy);width:180px}
.profile-text{position:absolute;left:16px;top:62px;width:175px;font-size:4.6px;line-height:1.6;color:var(--muted)}
.profile .photo{right:18px;top:26px;width:150px;height:150px;border-radius:50%;background:radial-gradient(circle at 50% 40%,#d9dee6,#9eabbd)}
.tabs{top:515px;height:26px;display:flex;justify-content:center;gap:3px;padding-top:6px}
.tab{width:42px;height:14px;border:1px solid var(--line);font-size:5px;display:flex;align-items:center;justify-content:center;color:var(--text);background:var(--white)}
.tab--active{background:var(--orange);border-color:var(--orange);color:var(--white)}
.roster{top:541px;height:211px;background:var(--grey);display:flex;gap:10px;padding:10px 16px}
.roster ul{flex:1;list-style:none}
.roster li{font-size:4.6px;color:var(--muted);line-height:1.55;border-bottom:1px solid var(--line)}
</style>
</head>
<body>

<section class="page page--home">
  <header class="band nav">
    <div class="brand">brolani<span class="brand-dot"></span></div>
    <nav class="nav-links"><span>Home</span><span>Company</span><span>Host Family</span><span>About</span></nav>
    <span class="nav-btn">Register</span>
  </header>

  <div class="band hero">
    <div class="photo" role="img" aria-label="Young apprentice working at a laptop in a bright office"></div>
    <div class="hero-copy">
      <h1>We offer apprenticeship exchanges within Switzerland and abroad</h1>
      <span class="btn">Read more</span>
    </div>
    <div class="dots"><i></i><i></i><i></i></div>
  </div>

  <section class="band features">
    <svg class="wave" style="top:0" viewBox="0 0 380 24" height="24"><path d="M0 0H380V6C280 26 120 -6 0 18Z" fill="#fff"/></svg>
    <h2>brolani</h2>
    <div class="icons">
      <div class="icon-item"><svg viewBox="0 0 26 26"><circle cx="13" cy="13" r="13" fill="#f36c21"/><rect x="7" y="10" width="12" height="8" rx="1" fill="#fff"/><rect x="10.5" y="7.5" width="5" height="3" fill="none" stroke="#fff" stroke-width="1.2"/></svg><span>Apprenticeships</span></div>
      <div class="icon-item"><svg viewBox="0 0 26 26"><circle cx="13" cy="13" r="13" fill="#f36c21"/><path d="M6 13L13 7l7 6v6H6z" fill="#fff"/></svg><span>Host Family</span></div>
      <div class="icon-item"><svg viewBox="0 0 26 26"><circle cx="13" cy="13" r="13" fill="#f36c21"/><circle cx="10" cy="10" r="2.5" fill="#fff"/><circle cx="16" cy="10" r="2.5" fill="#fff"/><path d="M5.5 19c0-4 9-4 9 0zM11.5 19c0-4 9-4 9 0z" fill="#fff"/></svg><span>Exchange</span></div>
      <div class="icon-item"><svg viewBox="0 0 26 26"><circle cx="13" cy="13" r="13" fill="#f36c21"/><rect x="8" y="7" width="10" height="12" fill="#fff"/><rect x="10" y="9" width="2" height="2" fill="#f36c21"/><rect x="14" y="9" width="2" height="2" fill="#f36c21"/><rect x="10" y="13" width="2" height="2" fill="#f36c21"/><rect x="14" y="13" width="2" height="2" fill="#f36c21"/></svg><span>Companies</span></div>
      <div class="icon-item"><svg viewBox="0 0 26 26"><circle cx="13" cy="13" r="13" fill="#f36c21"/><path d="M5 11l8-4 8 4-8 4z" fill="#fff"/><path d="M9 13v4c2 2 6 2 8 0v-4l-4 2z" fill="#fff"/></svg><span>Training</span></div>
    </div>
    <svg class="wave" style="bottom:0" viewBox="0 0 380 28" height="28"><path d="M0 28V14C120 30 260 -4 380 10V28Z" fill="#f36c21"/><path d="M0 28V20C140 32 260 6 380 18V28Z" fill="#fff"/></svg>
  </section>

  <section class="band intro">
    <p class="intro-text">We help young people find a work stage in another region of Switzerland or abroad. Apprentices gain new skills, learn another language and discover a new culture. We organise the match with a host company, travel and a stay with a host family, so every trainee can focus on learning and growing during the exchange.</p>
    <svg class="arc" style="right:28px;top:10px" width="174" height="174" viewBox="0 0 174 174"><path d="M20 130A78 78 0 0 1 150 30" fill="none" stroke="#f36c21" stroke-width="6"/></svg>
    <div class="photo" role="img" aria-label="Smiling apprentice in a blue shirt"></div>
  </section>

  <section class="band cards">
    <div class="card card--blue">
      <div class="card-badge"><svg width="12" height="12" viewBox="0 0 12 12"><path d="M2 6l3 3 5-6" stroke="#1f56a3" stroke-width="1.6" fill="none"/></svg></div>
      <h3>Project</h3>
      <p>Our programme connects apprentices with host companies across language regions. Stages last two to four weeks and are fully organised.</p>
    </div>
    <div class="card card--orange">
      <div class="card-badge"><svg width="12" height="12" viewBox="0 0 12 12"><circle cx="4" cy="4" r="2" fill="#f36c21"/><circle cx="8" cy="4" r="2" fill="#f36c21"/><path d="M1 10c0-3 6-3 6 0zM5 10c0-3 6-3 6 0z" fill="#f36c21"/></svg></div>
      <h3>Teams</h3>
      <p>A small volunteer team, a board and partners work together to match every young person with the right place.</p>
    </div>
  </section>

  <section class="band stories">
    <div class="photo" role="img" aria-label="Two apprentices at their workplaces"></div>
    <div class="stories-names">
      <h2>Nora<br>Kauffrau</h2>
      <h2>Jonas<br>Koch</h2>
    </div>
  </section>

  <section class="band mobility">
    <svg class="arc" style="left:14px;top:20px" width="154" height="154" viewBox="0 0 154 154"><path d="M20 40A70 70 0 0 1 134 40" fill="none" stroke="#f36c21" stroke-width="6"/><path d="M134 114A70 70 0 0 1 20 114" fill="none" stroke="#1f56a3" stroke-width="6"/></svg>
    <div class="photo" role="img" aria-label="Young apprentice smiling outdoors"></div>
    <div class="mobility-copy">
      <h3>Swiss Mobility:<br>Mobilität in der Schweiz</h3>
      <ul class="ticks">
        <li>Exchange between language regions</li>
        <li>Stages of two to four weeks</li>
        <li>Host families free of charge</li>
        <li>Support before and during the stay</li>
        <li>Open to all trades and sectors</li>
        <li>Certificate after the exchange</li>
      </ul>
    </div>
  </section>

  <section class="band apply apply--home">
    <svg width="44" height="38" viewBox="0 0 44 38"><rect x="2" y="2" width="30" height="26" rx="2" fill="none" stroke="#fff" stroke-width="2"/><path d="M8 10h18M8 16h18M8 22h10" stroke="#fff" stroke-width="2"/><path d="M30 26l10-10 3 3-10 10h-3z" fill="#fff"/></svg>
    <div>
      <h2>APPLY NOW!</h2>
      <span class="btn">Register</span>
    </div>
  </section>

  <footer class="band footer footer--home">
    <div class="footer-cols">
      <div class="footer-col"><div class="brand">brolani<span class="brand-dot"></span></div>info@lerntausch-brolani.ch<br>+41 31 555 01 20</div>
      <div class="footer-col"><h4>About</h4>Association for apprentice exchange in Switzerland and abroad, supported by Harmil Circle Switzerland.</div>
      <div class="footer-col"><h4>Login</h4><div class="field"></div><div class="field"></div></div>
    </div>
    <div class="partners"><span class="partner"></span><span class="partner"></span><span class="partner partner--round"></span></div>
    <div class="copyright">© brolani · www.lerntausch-brolani.ch</div>
  </footer>
</section>

<section class="page page--companies">
  <header class="band nav">
    <div class="brand">brolani<span class="brand-dot"></span></div>
    <nav class="nav-links"><span>Home</span><span>Company</span><span>Host Family</span><span>About</span></nav>
    <span class="nav-btn">Register</span>
  </header>

  <div class="band sub-hero">
    <div class="photo" role="img" aria-label="Apprentices at work in a company hall, blue tint"></div>
    <h1>APPRENDO SA TICINO</h1>
  </div>

  <section class="band companies">
    <div class="blueband"></div>
    <svg class="wave" style="top:18px" viewBox="0 0 380 24" height="24"><path d="M0 0H380V6C280 26 120 -6 0 18Z" fill="#fff"/></svg>
    <h2>COMPANIES</h2>
    <div class="icons">
      <div class="icon-item"><svg viewBox="0 0 26 26"><circle cx="13" cy="13" r="13" fill="#f36c21"/><rect x="8" y="7" width="10" height="12" fill="#fff"/></svg><span>Participating companies</span></div>
      <div class="icon-item"><svg viewBox="0 0 26 26"><circle cx="13" cy="13" r="13" fill="#f36c21"/><path d="M7 13l4 4 8-8" stroke="#fff" stroke-width="2" fill="none"/></svg><span>How to join</span></div>
      <div class="icon-item"><svg viewBox="0 0 26 26"><circle cx="13" cy="13" r="13" fill="#f36c21"/><rect x="7" y="10" width="12" height="8" rx="1" fill="#fff"/></svg><span>Send apprentices</span></div>
      <div class="icon-item"><svg viewBox="0 0 26 26"><circle cx="13" cy="13" r="13" fill="#f36c21"/><circle cx="13" cy="10" r="3" fill="#fff"/><path d="M7 19c0-5 12-5 12 0z" fill="#fff"/></svg><span>Host apprentices</span></div>
      <div class="icon-item"><svg viewBox="0 0 26 26"><circle cx="13" cy="13" r="13" fill="#f36c21"/><path d="M8 9h10v7h-6l-3 3v-3H8z" fill="#fff"/></svg><span>Contact us</span></div>
    </div>
    <svg class="wave" style="bottom:0" viewBox="0 0 380 28" height="28"><path d="M0 28V14C120 30 260 -4 380 10V28Z" fill="#f36c21"/><path d="M0 28V20C140 32 260 6 380 18V28Z" fill="#fff"/></svg>
  </section>

  <section class="band profile">
    <h2>Kessler Bauplan AG</h2>
    <p class="profile-text">Kessler Bauplan AG has taken part in the exchange for several years. The company sends its draughtsman apprentices to partner firms in other regions and welcomes young people from across the country. Trainees work on real projects, meet new colleagues and return with fresh ideas, more confidence and better language skills. The team values the programme as part of modern vocational training.</p>
    <svg class="arc" style="right:6px;top:14px" width="174" height="174" viewBox="0 0 174 174"><path d="M150 40A78 78 0 0 1 40 156" fill="none" stroke="#f36c21" stroke-width="6"/></svg>
    <div class="photo" role="img" aria-label="Architecture apprentice at a drawing desk"></div>
  </section>

  <nav class="band tabs">
    <span class="tab">2013</span><span class="tab">2014</span><span class="tab">2015</span><span class="tab">2016</span><span class="tab tab--active">2017</span><span class="tab">2018</span><span class="tab">2019</span>
  </nav>

  <section class="band roster">
    <ul><li>Alpen Holzbau AG</li><li>Berger Elektro GmbH</li><li>Café Lindenhof</li><li>Dach &amp; Wand AG</li><li>Eggli Sanitär</li><li>Frei Metallbau</li><li>Gasthaus Sonne</li><li>Huber Treuhand</li><li>Imhof Malerei</li><li>Jura Küchen AG</li><li>Keller Gartenbau</li><li>Lanz Schreinerei</li></ul>
    <ul><li>Meier Logistik AG</li><li>Nydegg Hotel</li><li>Oberli Bau AG</li><li>Pfister Design</li><li>Roth Informatik</li><li>Schmid Bäckerei</li><li>Tanner Optik</li><li>Ulrich Mechanik</li><li>Vogel Druck AG</li><li>Wyss Spenglerei</li><li>Zbinden Garage</li><li>Aebi Textil</li></ul>
    <ul><li>Bühler Möbel</li><li>Casa Verde SA</li><li>Dosch Elektro</li><li>Egger Planung</li><li>Fontana SA</li><li>Graf Hotellerie</li><li>Hess Kältetechnik</li><li>Iseli Fenster</li><li>Kunz Zimmerei</li><li>Lüthi Verlag</li><li>Moser Catering</li><li>Nef Architekten</li></ul>
  </section>

  <section class="band apply apply--companies">
    <svg width="52" height="46" viewBox="0 0 44 38"><rect x="2" y="2" width="30" height="26" rx="2" fill="none" stroke="#fff" stroke-width="2"/><path d="M8 10h18M8 16h18M8 22h10" stroke="#fff" stroke-width="2"/><path d="M30 26l10-10 3 3-10 10h-3z" fill="#fff"/></svg>
    <div>
      <h2>APPLY NOW!</h2>
      <span class="btn">Register</span>
    </div>
  </section>

  <footer class="band footer footer--companies">
    <div class="footer-cols">
      <div class="footer-col"><div class="brand">brolani<span class="brand-dot"></span></div>info@lerntausch-brolani.ch<br>+41 31 555 01 20<br>IBAN CH00 0000 0000 0000 0</div>
      <div class="footer-col"><h4>About</h4>Association for apprentice exchange in Switzerland and abroad, supported by Harmil Circle Switzerland.</div>
      <div class="footer-col"><h4>Login</h4><div class="field"></div><div class="field"></div><span class="btn" style="margin-top:2px">Send</span></div>
    </div>
    <div class="partners"><span class="partner"></span><span class="partner"></span><span class="partner partner--round"></span></div>
    <div class="copyright">© brolani · Harmil-Circle partner</div>
  </footer>
</section>

</body>
</html>
```